New web design for a service provider in the medical field

We are looking for a new design for our website. We are a company that repairs and sells medical endoscopes. Our customers include doctors and hospitals. Our current website can be found at https://lumenfix.example/en/lumenfix-english.
We need a new web design (without programming) for the following 3 pages:
-Startpage https://lumenfix.example/en/lumenfix-english/
-Used endoscopes https://lumenfix.example/en/used-endoscopes/
-Purchase https://lumenfix.example/en/purchase/
The design should be modern and stylish.
The blue color of the logo should be reflected on the page, but not too intrusive.
I have uploaded the images from the header. If more images are needed, let me know and I will upload them.

Target Market(s)
Doctors and hospitals

```html
<!DOCTYPE html>
<html lang="en">
<head>
<meta charset="utf-8">
<title>LumenFix – Endoscope Repair &amp; Sale</title>
<link rel="stylesheet" href="https://fonts.googleapis.com/css2?family=Manrope:wght@400;500;600;700;800&family=Inter:wght@400;500;600&display=swap">
<style>
  :root{
    --navy:#17344f;
    --navy-deep:#132c44;
    --blue:#2fa3e2;
    --blue-soft:#e9f5fc;
    --ice:#f4f9fd;
    --text:#4a5b6b;
    --muted:#8a98a6;
    --white:#ffffff;
    --line:#dce6ee;
  }
  *{box-sizing:border-box;margin:0;padding:0}
  html,body{width:1200px;height:3728px;overflow:hidden}
  body{background:var(--white);font-family:"Inter",sans-serif;color:var(--text);font-size:15px;line-height:1.6;position:relative}
  h1,h2,h3,h4,.brand,.btn,.nav a{font-family:"Manrope",sans-serif}
  .btn{display:inline-block;background:var(--blue);color:var(--white);font-size:13px;font-weight:700;padding:12px 28px;border-radius:30px;text-decoration:none;letter-spacing:.3px}
  .btn-dark{background:var(--navy)}
  .ph{background:linear-gradient(135deg,#e7eef3,#b9cad6);}
  .ph-circle{border-radius:50%;position:absolute}

  /* header */
  .site-header{position:absolute;top:0;left:0;width:1200px;height:620px;background:var(--white);overflow:hidden}
  .nav{position:absolute;top:28px;left:80px;right:80px;height:52px;display:flex;align-items:center;justify-content:space-between;z-index:3;background:rgba(255,255,255,.95);border-radius:30px;padding:0 28px;box-shadow:0 6px 20px rgba(23,52,79,.08)}
  .nav ul{display:flex;gap:28px;list-style:none}
  .nav a{color:var(--navy);font-size:13px;font-weight:600;text-decoration:none}
  .brand{display:flex;align-items:center;gap:8px;color:var(--navy);font-weight:800;font-size:20px}
  .brand .dot{width:14px;height:14px;border-radius:50%;background:var(--blue)}
  .nav-contact{font-size:12px;color:var(--muted)}
  .hero-photo{right:-140px;top:-60px;width:720px;height:720px;border:10px solid var(--blue-soft)}
  .hero-text{position:absolute;left:110px;top:210px;width:470px}
  .hero-text h1{font-size:50px;line-height:1.12;color:var(--navy);font-weight:500}
  .hero-text h1 strong{color:var(--blue);font-weight:800;letter-spacing:1px}
  .hero-text p{margin:22px 0 30px;font-size:15px}
  .hero-actions{display:flex;gap:14px;align-items:center}
  .round{width:44px;height:44px;border-radius:50%;background:var(--navy);display:flex;align-items:center;justify-content:center}

  /* service intro */
  .service-intro{position:absolute;top:640px;left:0;width:1200px;text-align:center}
  .service-intro h2{font-size:32px;color:var(--blue);font-weight:500}
  .service-intro h2 strong{color:var(--navy);font-weight:800}
  .service-intro p{width:720px;margin:16px auto 0}

  /* outcome band */
  .outcome-band{position:absolute;top:830px;left:0;width:1200px;height:420px;background:var(--ice)}
  .band-photo{left:80px;top:40px;width:340px;height:340px;border:8px solid var(--white)}
  .band-text{position:absolute;left:520px;top:70px;width:580px}
  .band-text h2{font-size:30px;line-height:1.25;color:var(--navy);font-weight:500}
  .band-text h2 strong{display:block;font-weight:800}
  .band-text p{margin-top:18px}

  /* cards */
  .services{position:absolute;top:1300px;left:110px;width:980px;display:flex;gap:40px}
  .card{flex:1;border-top:2px solid var(--line);padding-top:20px}
  .card h3{font-size:20px;color:var(--navy);font-weight:700}
  .card .thumb{width:150px;height:150px;border-radius:50%;margin:20px 0}
  .card p{font-size:14px;margin-bottom:22px}

  /* why band */
  .why{position:absolute;top:1740px;left:0;width:1200px;height:470px;background:var(--blue);color:var(--white);overflow:hidden}
  .why h2{position:absolute;left:110px;top:50px;font-size:34px;line-height:1.15;font-weight:500}
  .why h2 strong{display:block;font-weight:800}
  .why ul{position:absolute;left:110px;top:160px;list-style:none;width:520px}
  .why li{display:flex;gap:16px;align-items:flex-start;margin-bottom:16px}
  .why li svg{flex:none;margin-top:2px}
  .why li b{display:block;font-family:"Manrope",sans-serif;font-size:14px;letter-spacing:.4px;text-transform:uppercase}
  .why li span{font-size:13px;opacity:.85}
  .why-photo{right:-40px;top:40px;width:520px;height:520px;border:10px solid rgba(255,255,255,.35)}

  /* decision */
  .decision{position:absolute;top:2260px;left:0;width:1200px;height:560px}
  .decision header{text-align:center}
  .decision header p{font-size:26px;color:var(--blue);font-family:"Manrope",sans-serif}
  .decision header h2{font-size:32px;color:var(--navy);font-weight:800}
  .feature{position:absolute;width:300px}
  .feature h4{font-size:16px;color:var(--navy);margin:10px 0 6px}
  .feature p{font-size:13px}
  .f1{left:110px;top:170px}.f2{left:110px;top:350px}
  .f3{right:110px;top:170px;text-align:right}.f4{right:110px;top:350px;text-align:right}
  .f3 svg,.f4 svg{margin-left:auto;display:block}
  .product{position:absolute;left:440px;top:190px;width:320px;height:260px;border-radius:20px;background:linear-gradient(135deg,#f1f5f8,#d3dee6)}

  /* faulty */
  .faulty{position:absolute;top:2850px;left:0;width:1200px;height:600px;background:var(--ice);overflow:hidden}
  .faulty-photo{left:-60px;top:20px;width:480px;height:480px;border:10px solid var(--white)}
  .faulty-top{position:absolute;left:560px;top:60px}
  .faulty-top h2{font-size:32px;color:var(--navy);font-weight:500}
  .faulty-top h2 strong{color:var(--blue);font-weight:800}
  .faulty-top p{margin:10px 0 20px;font-size:14px}
  .contact-cta{position:absolute;left:480px;top:330px;width:620px}
  .contact-cta p{font-size:14px}
  .contact-cta h2{margin-top:34px;font-size:28px;line-height:1.25;color:var(--navy);font-weight:500}
  .contact-cta h2 strong{color:var(--blue);font-weight:800;display:block}
  .contact-cta .btn{position:absolute;right:0;bottom:6px}

  /* footer */
  .site-footer{position:absolute;top:3450px;left:0;width:1200px;height:278px;background:var(--navy-deep);color:#b7c6d4}
  .site-footer .brand{color:var(--white);position:absolute;left:110px;top:70px}
  .site-footer ul{position:absolute;right:110px;top:74px;display:flex;gap:34px;list-style:none;font-family:"Manrope",sans-serif;font-size:13px;font-weight:600;color:var(--white)}
  .site-footer small{position:absolute;right:110px;top:130px;font-size:12px}
  .site-footer hr{position:absolute;left:110px;right:110px;top:190px;border:0;border-top:1px solid rgba(255,255,255,.12)}
</style>
</head>
<body>

<header class="site-header">
  <nav class="nav">
    <ul>
      <li><a>Home</a></li>
      <li><a>Endoscope Repair</a></li>
      <li><a>Used Endoscopes</a></li>
    </ul>
    <div class="brand"><span class="dot"></span>LumenFix</div>
    <ul>
      <li><a>Purchase</a></li>
      <li><a>About Us</a></li>
      <li><a>Contact</a></li>
    </ul>
  </nav>
  <div class="ph ph-circle hero-photo" role="img" aria-label="Endoscope control handle held in a clinical setting"></div>
  <div class="hero-text">
    <h1>Put Your Scope in<br><strong>RELIABLE HANDS</strong></h1>
    <p>We repair, test and supply flexible and rigid endoscopes for clinics and practices – fast, certified and at fair prices.</p>
    <div class="hero-actions">
      <a class="btn">Learn more</a>
      <span class="round"><svg width="16" height="16" viewBox="0 0 16 16"><path d="M3 8h10M9 4l4 4-4 4" fill="none" stroke="#fff" stroke-width="2" stroke-linecap="round" stroke-linejoin="round"/></svg></span>
    </div>
  </div>
</header>

<section class="service-intro">
  <h2>Your Future - <strong>Our Service</strong></h2>
  <p>For more than twenty years we have kept endoscopes working for hospitals and doctors. Our team repairs every major model and returns your device quickly and safely.</p>
</section>

<section class="outcome-band">
  <div class="ph ph-circle band-photo" role="img" aria-label="Endoscope eyepiece and control body on a white surface"></div>
  <div class="band-text">
    <h2>Endoscope Repairs &amp;<br>Second Hand Endoscopes<br>from LumenFix -<strong>The Outcome Matters</strong></h2>
    <p>LumenFix is a specialised partner for the repair and sale of endoscopes. Every device passes a complete inspection before it goes back into use in your practice or clinic.</p>
    <p>Our technicians work to manufacturer standards, use quality parts and document each step, so you always know the condition of your equipment.</p>
  </div>
</section>

<section class="services">
  <article class="card">
    <h3>Repair</h3>
    <div class="ph thumb" role="img" aria-label="Technician repairing an endoscope"></div>
    <p>Fast and transparent repairs for flexible and rigid endoscopes, with a free cost estimate before any work begins.</p>
    <a class="btn btn-dark">Read more</a>
  </article>
  <article class="card">
    <h3>Sale</h3>
    <div class="ph thumb" role="img" aria-label="Refurbished endoscope ready for sale"></div>
    <p>Tested used endoscopes with warranty, a reliable and affordable alternative to buying brand new equipment.</p>
    <a class="btn btn-dark">Read more</a>
  </article>
  <article class="card">
    <h3>Purchase</h3>
    <div class="ph thumb" role="img" aria-label="Endoscope being handed over for purchase"></div>
    <p>We buy your used or defective endoscopes at fair prices and handle collection and paperwork for you.</p>
    <a class="btn">Read more</a>
  </article>
</section>

<section class="why">
  <h2>Cause The<strong>Outcome Matters!</strong></h2>
  <ul>
    <li><svg width="22" height="22" viewBox="0 0 22 22"><circle cx="11" cy="11" r="10" fill="#fff"/><path d="M6.5 11.5l3 3 6-6.5" fill="none" stroke="#2fa3e2" stroke-width="2" stroke-linecap="round"/></svg><div><b>Loan endoscopes available</b><span>Keep working while your device is in repair.</span></div></li>
    <li><svg width="22" height="22" viewBox="0 0 22 22"><circle cx="11" cy="11" r="10" fill="#fff"/><path d="M6.5 11.5l3 3 6-6.5" fill="none" stroke="#2fa3e2" stroke-width="2" stroke-linecap="round"/></svg><div><b>Experienced technicians</b><span>Specialists for all common manufacturers.</span></div></li>
    <li><svg width="22" height="22" viewBox="0 0 22 22"><circle cx="11" cy="11" r="10" fill="#fff"/><path d="M6.5 11.5l3 3 6-6.5" fill="none" stroke="#2fa3e2" stroke-width="2" stroke-linecap="round"/></svg><div><b>Free cost estimate</b><span>Clear prices before any repair starts.</span></div></li>
    <li><svg width="22" height="22" viewBox="0 0 22 22"><circle cx="11" cy="11" r="10" fill="#fff"/><path d="M6.5 11.5l3 3 6-6.5" fill="none" stroke="#2fa3e2" stroke-width="2" stroke-linecap="round"/></svg><div><b>Express service</b><span>Short turnaround times for urgent cases.</span></div></li>
    <li><svg width="22" height="22" viewBox="0 0 22 22"><circle cx="11" cy="11" r="10" fill="#fff"/><path d="M6.5 11.5l3 3 6-6.5" fill="none" stroke="#2fa3e2" stroke-width="2" stroke-linecap="round"/></svg><div><b>Warranty on repairs</b><span>Every repair is covered by our guarantee.</span></div></li>
  </ul>
  <div class="ph ph-circle why-photo" role="img" aria-label="Doctor in a white coat holding an endoscope"></div>
</section>

<section class="decision">
  <header>
    <p>LumenFix GmbH</p>
    <h2>Your Decision for Your Future</h2>
  </header>
  <div class="feature f1">
    <svg width="34" height="34" viewBox="0 0 34 34"><path d="M8 26l10-10m2-6l4 4-3 3-4-4z" fill="none" stroke="#17344f" stroke-width="2.4" stroke-linecap="round"/></svg>
    <h4>Fast repairs</h4><p>Most endoscopes are repaired and returned within a few working days.</p>
  </div>
  <div class="feature f2">
    <svg width="34" height="34" viewBox="0 0 34 34"><path d="M6 17L17 7l11 10v11H6z" fill="#17344f"/></svg>
    <h4>On-site service</h4><p>We collect and deliver devices directly to your practice or hospital.</p>
  </div>
  <div class="product" role="img" aria-label="Flexible endoscope with coiled insertion tube"></div>
  <div class="feature f3">
    <svg width="34" height="34" viewBox="0 0 34 34"><rect x="6" y="8" width="22" height="18" rx="3" fill="none" stroke="#17344f" stroke-width="2.4"/><path d="M11 17h12" stroke="#2fa3e2" stroke-width="2.4"/></svg>
    <h4>Highly cost-efficient</h4><p>Repair instead of replace and save a large share of new device costs.</p>
  </div>
  <div class="feature f4">
    <svg width="34" height="34" viewBox="0 0 34 34"><circle cx="17" cy="17" r="10" fill="none" stroke="#17344f" stroke-width="2.4"/><path d="M12 17l4 4 6-7" fill="none" stroke="#2fa3e2" stroke-width="2.4"/></svg>
    <h4>Loan equipment service</h4><p>Replacement devices bridge the time until your endoscope is back.</p>
  </div>
</section>

<section class="faulty">
  <div class="ph ph-circle faulty-photo" role="img" aria-label="Gloved hand holding an endoscope tip"></div>
  <div class="faulty-top">
    <h2>Faulty <strong>Endoscope?</strong></h2>
    <p>Send it to us today for a free inspection.</p>
    <a class="btn btn-dark">Start repair now</a>
  </div>
  <div class="contact-cta">
    <p>Our team is happy to advise you on repairs, used devices and purchases. Call us or write a short message and we will get back to you within one working day.</p>
    <h2>Do You Think We Can Help You?<strong>Feel Free to Contact Us!</strong></h2>
    <a class="btn">Contact</a>
  </div>
</section>

<footer class="site-footer">
  <div class="brand"><span class="dot"></span>LumenFix</div>
  <ul><li>Homepage</li><li>About</li><li>Contact</li><li>Imprint</li><li>Privacy</li></ul>
  <small>© LumenFix GmbH. All rights reserved.</small>
  <hr>
</footer>

</body>
</html>
```